Package Design for Chew Bone Guild for Marketora

Would like a label to put on a 6x9 package.

Here is my site: chewboneguild.example

Here are the labels I like:
https://rolfandkit.example/collections/bully-sticks/products/6-inch-standard-bully-sticks
https://www.marketora.example/stores/Rolf+%26+Kit/page/A1B2C3D4-5E6F-47A8-9B0C-1D2E3F4A5B6C?ref_=ast_bln
https://quiet-meadowland.example/amber-hound-junior-bully-sticks-6-25-pack/
https://www.wagsandwhimsy.example/shop/open-trailer-bully-stix

```html
<!DOCTYPE html>
<html lang="en">
<head>
<meta charset="utf-8">
<title>Chew Bone Guild – Premium Bully Sticks Pouch Label</title>
<link href="https://fonts.googleapis.com/css2?family=Fredoka:wght@500;600;700&display=swap" rel="stylesheet">
<style>
  :root {
    --backdrop: #0a1a21;
    --label-white: #f4f4f4;
    --pattern-grey: #e4e4e4;
    --ink-black: #0b0b0b;
    --rust: #a4523d;
    --rust-dark: #8a3e2c;
    --rust-light: #b86a55;
    --stick-dark: #3a1a12;
    --stick-mid: #7a3a1e;
    --stick-light: #a8612e;
    --numeral-grey: #cfcfcf;
    --cream: #fbeee8;
    --dog-brown: #9c4a36;
  }
  * { margin: 0; padding: 0; box-sizing: border-box; }
  html, body { width: 1200px; height: 835px; overflow: hidden; }
  body {
    background: var(--backdrop);
    font-family: "Fredoka", sans-serif;
    position: relative;
  }
  .pouch-label {
    position: absolute;
    left: 365px; top: 22px;
    width: 470px; height: 790px;
    background: var(--label-white);
    border-radius: 16px 16px 20px 20px;
    overflow: hidden;
  }
  .pattern-field {
    position: absolute; inset: 0 0 392px 0;
    background: linear-gradient(180deg, var(--label-white), var(--pattern-grey));
  }
  .brand-mark {
    position: absolute; left: 28px; top: 30px;
    display: flex; align-items: center; gap: 10px;
  }
  .brand-dot {
    width: 34px; height: 34px; border-radius: 50%;
    background: var(--rust);
  }
  .brand-name {
    font-weight: 600; font-size: 20px; color: var(--ink-black);
  }
  .grade-word {
    position: absolute; left: 153px; top: 104px;
    font-weight: 700; font-size: 34px; letter-spacing: 1px;
    color: var(--rust);
  }
  .product-title {
    position: absolute; left: 0; right: 0; top: 146px;
    text-align: center;
    font-weight: 700; font-size: 56px; letter-spacing: 1px;
    color: var(--ink-black);
  }
  .claim {
    position: absolute;
    font-weight: 600; font-size: 17px; line-height: 1.2;
    color: var(--rust);
    text-transform: uppercase;
  }
  .claim.left { left: 26px; }
  .claim.right { right: 30px; text-align: right; }
  .mascot-art {
    position: absolute; left: 141px; top: 245px;
    width: 171px; height: 155px;
    border-radius: 50% 50% 12px 12px;
    background: radial-gradient(circle at 50% 55%, #ffffff 0 42%, var(--dog-brown) 70%, #b0634c 100%);
  }
  .lower-panel {
    position: absolute; left: 0; top: 398px;
    width: 470px; height: 392px;
  }
  .size-numeral {
    position: absolute; left: 34px; top: 462px;
    font-weight: 600; font-size: 140px; line-height: 1;
    color: var(--numeral-grey);
  }
  .size-numeral sup { font-size: 56px; vertical-align: top; position: relative; top: 10px; }
  .panel-title {
    position: absolute; left: 42px; top: 628px;
    font-weight: 600; font-size: 40px; line-height: 1.15;
    color: #ececec;
  }
  .cert-line {
    position: absolute; left: 0; right: 0; top: 731px;
    text-align: center;
    font-weight: 600; font-size: 17px; line-height: 1.3;
    color: var(--cream);
    text-transform: uppercase;
  }
</style>
</head>
<body>
  <main class="pouch-label">
    <div class="pattern-field" role="img" aria-label="Light grey repeating pattern of dog bones and paw prints"></div>

    <div class="brand-mark">
      <span class="brand-dot"></span>
      <span class="brand-name">Chew Bone Guild</span>
    </div>

    <div class="grade-word">PEMEIUM</div>
    <h1 class="product-title">BULLY STICKS</h1>

    <p class="claim left" style="top:254px;">High in<br>Protein</p>
    <p class="claim left" style="top:324px;">For Dental<br>Health</p>
    <p class="claim right" style="top:254px;">Grass- Feed<br>Beef</p>
    <p class="claim right" style="top:324px;">Premium<br>Quality</p>

    <div class="mascot-art" role="img" aria-label="Cartoon puppy mascot with brown ears, blue collar and paws peeking over the band"></div>

    <svg class="lower-panel" viewBox="0 0 470 392" aria-hidden="false">
      <defs>
        <linearGradient id="stickTones" x1="0" x2="1" y1="0" y2="0">
          <stop offset="0" stop-color="var(--stick-dark)"/>
          <stop offset="0.3" stop-color="var(--stick-light)"/>
          <stop offset="0.55" stop-color="var(--stick-mid)"/>
          <stop offset="0.8" stop-color="var(--stick-light)"/>
          <stop offset="1" stop-color="var(--stick-dark)"/>
        </linearGradient>
      </defs>
      <rect x="0" y="0" width="470" height="15" fill="var(--rust-dark)"/>
      <rect x="0" y="15" width="470" height="305" fill="var(--ink-black)"/>
      <g role="img" aria-label="Photo of a row of six-inch bully sticks">
        <path d="M150,15 Q95,170 172,320 L450,320 L450,15 Z" fill="url(#stickTones)"/>
      </g>
      <path d="M150,15 Q95,170 172,320" fill="none" stroke="var(--rust)" stroke-width="3"/>
      <rect x="0" y="320" width="470" height="72" fill="var(--rust-light)"/>
    </svg>

    <div class="size-numeral">6<sup>″</sup></div>
    <div class="panel-title">BULLY<br>STICKS</div>
    <p class="cert-line">USDA Certified,<br>Inspected &amp; Approved</p>
  </main>
</body>
</html>
```